wine label for ultra premium vineyard in Bendigo, Central Otago, New Zealand

"WREN" is our new wine brand, with grapes grown in our spectacular "ter Bosch" vineyard. The small, elevated vineyard overlooks a river valley and snowy mountains. We would like a highly elegant label for our 2018 pinot noir wine, which highlights the quality of wine and our very special vineyard location. "WREN" has to be prominent, with secondary emphasis on "ter Bosch vineyard" and "Bendigo, Central Otago". A stylized WREN logo (bird) could be a useful design device instead of the commonly seen illustrated mountain landscape (which is quite common for our local wines). Label size 90 high, 110 wide. Please use a pinot noir / burgundy bottle. See here for vineyard pics, and also below pics for other local wine labels and pics for inspiration / styles. https://www.instagram.com/jan.ter.bosch/

Target Market(s)

average bottle price for this premium red pinot noir would be aroundUS$40. target market are generally urban professionals aged 25 and older with a high degree of interest in pinot noir wine, and who are familiar with New Zealand pinot noir (ie. already know several brands).

Colors
ed252d

Requirements
Must have
• distinctive label, sophisticated look
Nice to have
• classy white paper stock
Should not have
• label must not get too busy... less but high quality and distinctive is more....

```html
<!DOCTYPE html>
<html lang="en">
<head>
<meta charset="utf-8">
<title>WREN – ter Bosch vineyard pinot noir label</title>
<link rel="stylesheet" href="https://fonts.googleapis.com/css2?family=Cabin:wght@400;700&family=Fira+Mono&display=swap">
<style>
  :root {
    --brand-red: #ed252d;
    --deep-red: #7a1212;
    --paper: #efefec;
    --paper-shade: #e6e6e2;
    --gold-dark: #c98a0e;
    --gold-mid: #e8b420;
    --gold-light: #f7dc6a;
    --page: #ffffff;
  }
  * { margin: 0; padding: 0; box-sizing: border-box; }
  html, body {
    width: 950px;
    height: 1200px;
    overflow: hidden;
    background: var(--page);
  }
  .canvas {
    position: relative;
    width: 950px;
    height: 1200px;
  }

  /* ---------- flat label ---------- */
  .label {
    position: absolute;
    left: 197px;
    top: 60px;
    width: 556px;
    height: 679px;
    background: radial-gradient(ellipse at 50% 40%, var(--paper) 0%, var(--paper-shade) 100%);
    text-align: center;
  }
  .gold-band {
    position: absolute;
    top: 0;
    width: 30px;
    height: 100%;
    background: linear-gradient(170deg,
      var(--gold-dark) 0%, var(--gold-light) 18%, var(--gold-mid) 35%,
      var(--gold-dark) 52%, var(--gold-light) 70%, var(--gold-mid) 85%, var(--gold-dark) 100%);
  }
  .gold-band--left { left: 0; }
  .gold-band--right { right: 0; }

  .label__bird {
    position: absolute;
    left: 195px;
    top: 50px;
    width: 165px;
    height: 161px;
    border-radius: 50%;
    background: radial-gradient(circle, rgba(237,37,45,0.85) 0%, rgba(237,37,45,0.35) 55%, rgba(237,37,45,0) 72%);
  }
  .label__brand {
    position: absolute;
    left: 0;
    right: 0;
    top: 262px;
    font-family: "Cabin", sans-serif;
    font-weight: 700;
    font-size: 76px;
    line-height: 1;
    letter-spacing: 8px;
    color: var(--brand-red);
  }
  .label__variety {
    position: absolute;
    left: 0;
    right: 0;
    top: 380px;
    font-family: "Fira Mono", monospace;
    font-size: 22px;
    line-height: 33px;
    color: var(--brand-red);
    letter-spacing: 1px;
  }
  .label__vineyard {
    position: absolute;
    left: 0;
    right: 0;
    top: 500px;
    font-family: "Cabin", sans-serif;
    font-weight: 700;
    font-size: 33px;
    line-height: 37px;
    color: var(--deep-red);
    letter-spacing: 0.5px;
  }
  .label__region {
    position: absolute;
    left: 0;
    right: 0;
    top: 608px;
    font-family: "Cabin", sans-serif;
    font-size: 21px;
    color: var(--deep-red);
    letter-spacing: 0.5px;
  }

  /* ---------- brand lock-up ---------- */
  .lockup__bird {
    position: absolute;
    left: 365px;
    top: 780px;
    width: 223px;
    height: 217px;
    border-radius: 50%;
    background: radial-gradient(circle, rgba(237,37,45,0.85) 0%, rgba(237,37,45,0.35) 55%, rgba(237,37,45,0) 72%);
  }
  .lockup__brand {
    position: absolute;
    left: 0;
    right: 0;
    top: 1015px;
    text-align: center;
    font-family: "Cabin", sans-serif;
    font-weight: 700;
    font-size: 104px;
    line-height: 1;
    letter-spacing: 10px;
    color: var(--brand-red);
  }
</style>
</head>
<body>
<div class="canvas">
  <section class="label">
    <div class="gold-band gold-band--left"></div>
    <div class="gold-band gold-band--right"></div>
    <div class="label__bird" role="img" aria-label="Red textured illustration of a small bird in flight"></div>
    <h1 class="label__brand">WREN</h1>
    <p class="label__variety">premium<br>red pinot noir</p>
    <h2 class="label__vineyard">ter Bosch<br>vineyard</h2>
    <p class="label__region">Bendigo, Central Otago</p>
  </section>

  <div class="lockup__bird" role="img" aria-label="Red textured illustration of a small bird in flight"></div>
  <div class="lockup__brand">WREN</div>
</div>
</body>
</html>
```